VELORA Group Fitness Class Launch Poster!

We need a poster design for a upcoming Group Fitness Class launch with two additional social media post designs.
Please follow our Brand Style Guide, as I will not be able to accept anything outside of this guide.
Class Description:
Come and VELORA your body with this class while catching up with friends and meeting new people. It is low-impact strength training with bodyweight exercises to help improve muscular strength, cardiovascular endurance, balance, bone health and functional training. It is suitable for all fitness levels.
Class Length: 30 Minutes
Intro script for class online:
📣New class alert❗
TPW team is excited to announce the launch of our new class, "VELORA", instructed by Jo! 🥰
Unsure if group fitness classes are for you? Join us for 30-minute low-impact strength training with bodyweight exercises! It's time to build your confidence in a fun and supportive environment.
Target Market(s)
Target audience is mostly females which barrier to entry to fitness is not having the confidence to join or has limited capability and needing low impact. Important to note that our demographic tends to be below 50... So barriers is most likely to be confidence, overweight or unfit.
Industry/Entity Type
Fitness
Other font styles liked:
- Please follow the Style Guide Fonts.
Requirements
Must have
- The project must follow our Brand Guidelines & include the class logo. Poster should be exciting and stand out. Don't necessarily have to use the stock images provided.
Should not have
- If you select your own image, the preference would be that it does not only include slim/fit looking individuals.

```html
<!DOCTYPE html>
<html lang="en">
<head>
<meta charset="utf-8">
<title>VELORA – New Class Poster</title>
<link href="https://fonts.googleapis.com/css2?family=Noto+Serif:wght@300;800;900&family=Figtree:ital,wght@0,400;0,500;1,800&display=swap" rel="stylesheet">
<style>
  :root {
    --ink: #121212;
    --ink-soft: #1d1d1d;
    --brand-red: #a51f2d;
    --photo-light: #c2575c;
    --photo-mid: #9a3a40;
    --photo-dark: #6e2228;
    --white: #ffffff;
  }
  * { margin: 0; padding: 0; box-sizing: border-box; }
  html, body { width: 848px; height: 1200px; overflow: hidden; background: var(--ink); }
  .poster {
    position: relative; width: 848px; height: 1200px; overflow: hidden;
    background: radial-gradient(ellipse at 50% 70%, var(--ink-soft), var(--ink) 70%);
    color: var(--white);
    font-family: "Figtree", Arial, sans-serif;
  }
  .hero-photo { position: absolute; left: 0; top: 0; width: 848px; height: 560px; }
  .headline {
    position: absolute; left: 0; width: 100%; top: 162px; text-align: center;
    font-family: "Noto Serif", Georgia, serif; font-weight: 900;
    font-size: 66px; line-height: 76px; letter-spacing: 1px;
  }
  .intro {
    position: absolute; left: 110px; width: 628px; top: 323px; text-align: center;
    font-weight: 500; font-size: 14.5px; line-height: 18.8px;
  }
  .class-length {
    position: absolute; left: 0; width: 100%; top: 588px; text-align: center;
    font-family: "Noto Serif", Georgia, serif; font-weight: 300; font-size: 38px;
  }
  .script-label {
    position: absolute; left: 0; width: 100%; top: 642px; text-align: center; font-size: 17.5px;
  }
  .alert-banner { position: absolute; left: 244px; top: 694px; width: 366px; height: 80px; }
  .alert-text {
    position: absolute; left: 244px; top: 707px; width: 366px; text-align: center;
    font-style: italic; font-weight: 800; font-size: 40px; line-height: 50px;
  }
  .megaphone { position: absolute; top: 700px; width: 116px; height: 90px; }
  .megaphone--left { left: 96px; }
  .megaphone--right { left: 638px; transform: scaleX(-1); }
  .announcement {
    position: absolute; left: 0; width: 100%; top: 802px; text-align: center;
    font-size: 21px; line-height: 26px;
  }
  .question {
    position: absolute; left: 0; width: 100%; top: 890px; text-align: center;
    font-family: "Noto Serif", Georgia, serif; font-weight: 800; font-size: 37px; line-height: 40px;
  }
  .brand-mark { position: absolute; left: 130px; top: 1010px; width: 240px; height: 110px; }
  .brand-mark__dot {
    position: absolute; left: 60px; top: 0; width: 64px; height: 64px; border-radius: 50%;
    background: var(--brand-red);
  }
  .brand-mark__name {
    position: absolute; left: 0; top: 62px; width: 240px; text-align: center;
    font-weight: 500; font-size: 22px; line-height: 24px; color: var(--white);
  }
  .invite {
    position: absolute; left: 443px; top: 1002px; width: 330px;
    font-size: 19.5px; line-height: 24.3px;
  }
</style>
</head>
<body>
<main class="poster">
  <svg class="hero-photo" viewBox="0 0 848 560" role="img" aria-label="Red-tinted photo of three people of different body types doing bodyweight squats in a gym">
    <defs>
      <linearGradient id="photoTone" x1="0" y1="0" x2="0" y2="1">
        <stop offset="0" stop-color="var(--photo-mid)"/>
        <stop offset="0.45" stop-color="var(--photo-light)"/>
        <stop offset="1" stop-color="var(--photo-dark)"/>
      </linearGradient>
    </defs>
    <polygon fill="url(#photoTone)" points="0,0 848,0 848,380 800,420 770,455 700,480 600,485 560,470 430,520 300,545 290,470 230,480 190,450 120,395 60,385 0,360"/>
    <polyline fill="none" stroke="var(--brand-red)" stroke-width="6" points="0,365 60,389 120,399 190,455 230,485 296,473 300,550 430,525 560,476 600,490 700,486 770,460 800,425 848,385"/>
  </svg>

  <h1 class="headline">COME AND<br>VELORA WITH US</h1>
  <p class="intro">with this class while catching up with friends and meeting new people. It is low-impact strength training with bodyweight exercises to help improve muscular strength, cardiovascular endurance, balance, bone health and functional training. It is suitable for all fitness levels.</p>

  <h2 class="class-length">Class Length: 30 Minutes</h2>
  <p class="script-label">intro script for class online:</p>

  <svg class="megaphone megaphone--left" viewBox="0 0 116 90" aria-hidden="true">
    <g fill="var(--white)">
      <rect x="4" y="38" width="10" height="20" rx="3"/>
      <polygon points="14,34 60,10 64,10 64,84 60,84 14,60"/>
      <polygon points="26,60 38,64 32,86 22,84"/>
    </g>
    <g fill="none" stroke="var(--white)" stroke-width="5" stroke-linecap="round">
      <path d="M76 30 Q84 47 76 64"/>
      <path d="M88 22 Q100 47 88 72"/>
      <path d="M100 14 Q116 47 100 80"/>
    </g>
  </svg>

  <svg class="alert-banner" viewBox="0 0 366 80" aria-hidden="true">
    <polygon fill="var(--brand-red)" points="6,4 120,0 250,5 362,2 366,40 360,78 240,74 120,79 2,76 0,40"/>
  </svg>
  <p class="alert-text">New class alert</p>

  <svg class="megaphone megaphone--right" viewBox="0 0 116 90" aria-hidden="true">
    <g fill="var(--white)">
      <rect x="4" y="38" width="10" height="20" rx="3"/>
      <polygon points="14,34 60,10 64,10 64,84 60,84 14,60"/>
      <polygon points="26,60 38,64 32,86 22,84"/>
    </g>
    <g fill="none" stroke="var(--white)" stroke-width="5" stroke-linecap="round">
      <path d="M76 30 Q84 47 76 64"/>
      <path d="M88 22 Q100 47 88 72"/>
      <path d="M100 14 Q116 47 100 80"/>
    </g>
  </svg>

  <p class="announcement">TPW team is excited to announce the launch of our<br>new class, "VELORA", instructed by Jo!</p>

  <h2 class="question">UNSURE IF GROUP FITNESS<br>CLASSES ARE FOR YOU?</h2>

  <div class="brand-mark">
    <span class="brand-mark__dot"></span>
    <p class="brand-mark__name">Redgum Shire<br>Recreation &amp; Fitness</p>
  </div>

  <p class="invite">Join us for 30-minute low-impact strength training with bodyweight exercises! It's time to build your confidence in a fun and supportive environment.</p>
</main>
</body>
</html>
```